American Ingenuity + Italian Design = RTB
International consulting services from fine arts/advertising/construction & special events. A new company that will find the right connections to get your job done.

Card should include -
1. Company Name with logo: rosalind tavera Enterprises LLC
2. Address: 218 Marlow Bend, Highland Springs, VA 23091
3. Phone Number: 804.555.2164 (US)
4. Tagline: American Ingenuity + Italian Style + RTB (you can improve on this idea)
5. web address to be added eventually

Likes: airplanes and boats to give the idea of movement & international ability
Logo: if you have an idea to adjust the colors, we are open to that. Rosalind likes blues, but other colors didn't seem to work; remember this will print 4c in most cases)
Updates

I have uploaded the logo on it's own. Typical business card size for the US is 3.5" x 2", but doesn't have to be that size. the flyer was just for reference of something else that was done and to give some background. I hope that didn't confuse anyone.

Thank you all for the amazing work in the tight deadline. We will be reviewing everything today and will provide feedback by tomorrow. I will also pass this site on to anyone I know looking for design work.

website address rosalindtavera.example email rosalind@rosalindtavera.example Italian number +39 333 581 0492 USA 1 804 555 2164 International Consulting Services American Ingenuity. Italian Design. rtB These are the vital elements for the card. In addition please note the new fotos should have been uploaded. Best Regards

Target Market(s)

Companies or individuals that want to bring the Italian flair to the US or American know how to Italian projects. This can range from a bride planning a destination wedding, an interior designer looking to add pieces or knowledge to their project, or an investor looking to buy property to invest and build.

Industry/Entity Type

Construction

Requirements
Must have
• 1. Company Name with logo: rosalind tavera Enterprises LLC
+39 333 581 0492 (Italia)
Nice to have
• incorporate the idea of international ability; airplanes (like the wing in the background of the logo)
Should not have
• not overly decorative

```html
<!DOCTYPE html>
<html lang="en">
<head>
<meta charset="utf-8">
<title>rosalind tavera Enterprises LLC – Business Card</title>
<link rel="stylesheet" href="https://fonts.googleapis.com/css2?family=Open+Sans:wght@400&display=swap">
<style>
  :root {
    --backdrop: #e9e6e1;
    --card-white: #ffffff;
    --brand-red: #8e3a2e;
    --brand-red-dark: #6e2a20;
    --brand-blue: #3d5a92;
    --brand-maroon: #5a1712;
    --sky-top: #4a6fa8;
    --sky-mid: #c98a63;
    --sky-glow: #f3c488;
    --cloud-low: #4b2e3c;
    --text-light: #ffffff;
  }
  * { margin: 0; padding: 0; box-sizing: border-box; }
  html, body {
    width: 1200px;
    height: 784px;
    overflow: hidden;
    background: var(--backdrop);
    font-family: "Open Sans", Arial, sans-serif;
  }
  .canvas {
    position: relative;
    width: 1200px;
    height: 784px;
  }
  .card {
    position: absolute;
    width: 540px;
    height: 309px;
    overflow: hidden;
    box-shadow: 0 6px 18px rgba(0,0,0,0.18);
  }

  /* Front of card */
  .card-front {
    left: 50px;
    top: 80px;
  }
  .sky-photo {
    position: absolute;
    inset: 0;
    background:
      radial-gradient(ellipse 35% 30% at 62% 40%, var(--sky-glow) 0%, rgba(243,196,136,0) 100%),
      linear-gradient(180deg, var(--sky-top) 0%, #7d86a6 30%, var(--sky-mid) 52%, #8a5a5e 68%, var(--cloud-low) 100%);
  }
  .front-brand {
    position: absolute;
    left: 0;
    right: 0;
    top: 92px;
    text-align: center;
    color: var(--brand-maroon);
    font-size: 27px;
    letter-spacing: 0.5px;
  }
  .front-tagline {
    position: absolute;
    left: 0;
    right: 0;
    bottom: 42px;
    text-align: center;
    color: var(--text-light);
    font-size: 16px;
    letter-spacing: 3px;
  }

  /* Back of card */
  .card-back {
    left: 610px;
    top: 390px;
    background: var(--card-white);
  }
  .back-swoosh {
    position: absolute;
    inset: 0;
    width: 540px;
    height: 309px;
  }
  .back-brand {
    position: absolute;
    right: 34px;
    top: 52px;
    width: 300px;
    text-align: right;
    color: var(--brand-maroon);
    font-size: 19px;
    line-height: 1.25;
  }
  .contact-list {
    position: absolute;
    left: 30px;
    bottom: 22px;
    list-style: none;
    color: var(--text-light);
    font-size: 14px;
  }
  .contact-item {
    display: flex;
    align-items: center;
    gap: 8px;
    line-height: 23px;
  }
  .contact-icon {
    width: 13px;
    height: 13px;
    flex: none;
  }
</style>
</head>
<body>
<main class="canvas">

  <section class="card card-front" aria-label="Business card front">
    <div class="sky-photo" role="img" aria-label="Photograph of an airplane wing above the clouds at sunset"></div>
    <p class="front-brand">rosalind tavera Enterprises LLC</p>
    <p class="front-tagline">American Ingenuity + Italian Style = RTB</p>
  </section>

  <section class="card card-back" aria-label="Business card back">
    <svg class="back-swoosh" viewBox="0 0 540 309" aria-hidden="true">
      <path d="M0 150 C 90 175, 200 190, 300 190 C 390 190, 470 175, 540 160 L540 309 L0 309 Z" fill="var(--brand-red)"/>
      <path d="M0 150 C 70 168, 150 180, 240 186 C 160 178, 80 168, 0 160 Z" fill="var(--card-white)"/>
      <path d="M0 130 C 80 160, 170 178, 260 182 C 170 172, 80 152, 0 140 Z" fill="var(--brand-blue)"/>
      <path d="M0 150 C 90 175, 200 190, 300 190 C 390 190, 470 175, 540 160 L540 170 C 470 186, 390 200, 300 200 C 200 200, 90 186, 0 162 Z" fill="var(--brand-red-dark)" opacity="0.35"/>
    </svg>

    <p class="back-brand">rosalind tavera Enterprises LLC</p>

    <ul class="contact-list">
      <li class="contact-item">
        <svg class="contact-icon" viewBox="0 0 16 16" aria-hidden="true"><path d="M3 1 L6 1 L7 5 L5 6.5 C6 9 7 10 9.5 11 L11 9 L15 10 L15 13 C15 14 14 15 13 15 C6 15 1 10 1 3 C1 2 2 1 3 1 Z" fill="var(--text-light)"/></svg>
        <span>804.555.2164 (US)</span>
      </li>
      <li class="contact-item">
        <svg class="contact-icon" viewBox="0 0 16 16" aria-hidden="true"><circle cx="8" cy="8" r="6.5" fill="none" stroke="var(--text-light)" stroke-width="1.4"/><ellipse cx="8" cy="8" rx="2.8" ry="6.5" fill="none" stroke="var(--text-light)" stroke-width="1.2"/><line x1="1.5" y1="8" x2="14.5" y2="8" stroke="var(--text-light)" stroke-width="1.2"/></svg>
        <span>www.rosalindtaveraenterprises.example</span>
      </li>
      <li class="contact-item">
        <svg class="contact-icon" viewBox="0 0 16 16" aria-hidden="true"><path d="M8 1.5 L15 8 L13 8 L13 14.5 L9.5 14.5 L9.5 10 L6.5 10 L6.5 14.5 L3 14.5 L3 8 L1 8 Z" fill="var(--text-light)"/></svg>
        <span>218 Marlow Bend, Highland Springs, VA 23091</span>
      </li>
    </ul>
  </section>

</main>
</body>
</html>
```